Flyer design for webdesign company

create a flyer that can be printed or sent as an email. The flyer needs to be professional, modern and engaging.

Reason: opportunity for all designers to get their designs in.

Target Market(s)

business owners that do not have a website

Industry/Entity Type

It Company

Font styles to use
Sans Serif

```html
<!DOCTYPE html>
<html lang="en">
<head>
<meta charset="utf-8">
<title>Vertexsites Flyer</title>
<link rel="stylesheet" href="https://fonts.googleapis.com/css2?family=Bebas+Neue&family=Cabin:wght@400;500&family=Lato:wght@300;400&display=swap">
<style>
  :root{
    --orange:#e98a30;
    --cream:#fdeadb;
    --ink:#505559;
    --ink-soft:#5a5e63;
    --sky:#8ad6f7;
    --ring:#8fc3e6;
    --panel:#ffffff;
    --side:#ececec;
    --page:#ffffff;
    --suit:#1a2230;
    --steel:#3d5f80;
    --glow:#e6f6ff;
    --screen:#5fb8ea;
  }
  *{margin:0;padding:0;box-sizing:border-box}
  html,body{width:1200px;height:1200px;overflow:hidden;background:var(--page)}
  .flyer{position:absolute;left:54px;top:127px;width:1087px;height:839px;background:var(--side);overflow:hidden}
  .hero{position:absolute;left:0;top:0;width:1087px;height:584px;
    background:
      radial-gradient(ellipse 150px 120px at 56% 34%, rgba(230,246,255,.95) 0%, rgba(160,210,240,.55) 45%, rgba(90,150,200,0) 100%),
      radial-gradient(ellipse 190px 110px at 58% 90%, rgba(235,242,250,.9) 0%, rgba(190,210,228,.55) 50%, rgba(150,180,210,0) 100%),
      radial-gradient(ellipse 150px 140px at 18% 45%, rgba(95,184,234,.85) 0%, rgba(95,184,234,.35) 55%, rgba(95,184,234,0) 100%),
      radial-gradient(ellipse 230px 90px at 85% 73%, rgba(120,200,240,.9) 0%, rgba(95,184,234,.4) 55%, rgba(95,184,234,0) 100%),
      radial-gradient(ellipse 130px 90px at 80% 20%, rgba(150,215,245,.8) 0%, rgba(95,184,234,.3) 60%, rgba(95,184,234,0) 100%),
      radial-gradient(ellipse 240px 200px at 97% 10%, rgba(160,190,215,.7) 0%, rgba(160,190,215,0) 100%),
      radial-gradient(ellipse 520px 380px at 52% 48%, #6d9cc2 0%, var(--steel) 45%, #243247 80%, var(--suit) 100%)}
  .panel{position:absolute;left:14px;top:584px;width:1058px;height:235px;background:var(--panel)}
  .band{position:absolute;left:0;top:819px;width:1087px;height:20px;background:var(--sky)}
  .ring{position:absolute;border:1px solid var(--ring);border-radius:50%}
  .disc{position:absolute;border-radius:50%;display:flex;flex-direction:column;align-items:center;justify-content:center;text-align:center}
  .headline{left:42px;top:327px;width:364px;height:364px;background:var(--orange);color:var(--cream);font-family:'Bebas Neue',sans-serif;line-height:.86}
  .headline .small{font-size:80px}
  .headline .big{font-size:190px;margin:4px 0 6px}
  .headline .mid{font-size:62px}
  .price-badge{left:900px;top:31px;width:152px;height:152px;background:var(--orange);color:var(--cream);font-family:'Bebas Neue',sans-serif;font-size:50px;line-height:.9}
  .brand{left:790px;top:350px;width:208px;height:208px;background:#fff;gap:10px}
  .brand .dot{width:26px;height:26px;border-radius:50%;background:var(--orange)}
  .brand .name{font-family:'Cabin',sans-serif;font-size:24px;color:var(--orange);font-weight:500}
  .tagline{position:absolute;left:380px;top:592px;width:706px;text-align:center;font-family:'Cabin',sans-serif;font-size:25px;color:var(--ink)}
  .offer{position:absolute;left:536px;top:616px;font-family:'Bebas Neue',sans-serif;color:var(--orange);font-size:63px;white-space:nowrap}
  .offer small{font-size:17px;color:#222;margin-left:6px;vertical-align:18px}
  .contact{position:absolute;left:380px;top:684px;width:655px;text-align:right;font-family:'Lato',sans-serif;font-weight:300;font-size:28px;color:var(--ink-soft);white-space:nowrap}
  .features{position:absolute;left:14px;top:731px;width:1058px;height:74px;display:flex}
  .feature{text-align:center;font-family:'Lato',sans-serif;font-weight:300;font-size:15.5px;line-height:1.35;color:var(--ink)}
  .feature:nth-child(1){width:265px}
  .feature:nth-child(2){width:271px}
  .feature:nth-child(3){width:280px}
  .feature:nth-child(4){width:242px}
  .feature + .feature{border-left:1px solid #bdbdbd}
  .feature h3{font-family:'Bebas Neue',sans-serif;font-weight:400;font-size:34px;line-height:1;color:var(--orange);margin-bottom:1px}
</style>
</head>
<body>
  <main class="flyer">
    <div class="hero" role="img" aria-label="Photo of open hands holding a glowing globe with laptop, phone and tablet surrounded by social network icons"></div>
    <div class="panel"></div>
    <div class="band"></div>

    <div class="ring" style="left:28px;top:313px;width:392px;height:392px"></div>
    <div class="disc headline">
      <span class="small">Attract</span>
      <span class="big">More</span>
      <span class="mid">Customers</span>
    </div>

    <div class="ring" style="left:892px;top:23px;width:168px;height:168px;border-color:#cfe6f6"></div>
    <div class="disc price-badge"><span>Only $3</span><span>A Day</span></div>

    <div class="ring" style="left:778px;top:338px;width:232px;height:232px;border-color:#cfe6f6"></div>
    <div class="disc brand">
      <span class="dot"></span>
      <span class="name">vertexsites</span>
    </div>

    <p class="tagline">Stop Wasting Money On Mailers And Print Advertising</p>
    <p class="offer">Only $99 / Month<small>(No other costs)</small></p>
    <p class="contact">Call today 1-800-555-0142 • www.yoursitenow.com</p>

    <section class="features">
      <div class="feature"><h3>97%</h3>Of people look online for<br>businesses. You need a website.</div>
      <div class="feature"><h3>Beat</h3>your competition with<br>better visibility and credibility</div>
      <div class="feature"><h3>Smart</h3>clean website designs<br>($3000 value. No extra charge)</div>
      <div class="feature"><h3>Social Media</h3>set up options<br>(Findr and Linkbook).</div>
    </section>
  </main>
</body>
</html>
```